Banner Ad Design Project

This is a banner Ad Design for MindHarbor 2013, a conference and e-Expo in August 2013 to be held at the Kestrel Bay Events Centre. The conference's focus is on mental excellence and Brain Health. This conference is bringing together personal and community needs, scientific knowledge, and dedicated professionals to create support and solutions for mental excellence and brain-related health issues. Right now in North America, one out of every two individuals is affected by mental health issues: depression, anxiety, learning disorders, memory loss to name a few.
Who we are:
Organization: Willow Lantern Foundation
Industry: Non-profit
Target Market(s)
Age group above 18, parents and health professionals, managers.
Industry/Entity Type
Mental Health
Requirements
Must have
- Please follow the warm design grey as in the design samples.
Nice to have
- Buy tickets and ask your unique questions to the medical panel! Seats are limited!

```html
<!DOCTYPE html>
<html lang="en">
<head>
<meta charset="utf-8">
<title>MindHarbor 2013 – Banner</title>
<link rel="stylesheet" href="https://fonts.googleapis.com/css2?family=PT+Sans:wght@400;700&display=swap">
<style>
  :root {
    --navy: #1d3e7a;
    --orange-deep: #ef8410;
    --orange-mid: #f59a1b;
    --orange-light: #f9b63a;
    --panel-white: #ffffff;
    --shadow-grey: #c9c9c9;
    --purple-top: #b14ee0;
    --purple-bottom: #7d1fb8;
    --purple-edge: #5e1690;
    --white: #ffffff;
    --brand-dot: #7fb0e0;
  }
  * { margin: 0; padding: 0; box-sizing: border-box; }
  html, body { width: 1200px; height: 148px; overflow: hidden; background: var(--panel-white); }
  .banner {
    position: relative;
    width: 1200px;
    height: 148px;
    overflow: hidden;
    font-family: "PT Sans", Arial, sans-serif;
    background: linear-gradient(90deg, var(--orange-deep) 25%, var(--orange-mid) 55%, var(--orange-light) 100%);
  }
  .banner__backdrop { position: absolute; inset: 0; }
  .brand {
    position: absolute;
    left: 24px;
    top: 40px;
    display: flex;
    align-items: center;
    gap: 14px;
    color: var(--navy);
  }
  .brand__dot {
    flex: none;
    width: 54px;
    height: 54px;
    border-radius: 50%;
    background: var(--brand-dot);
  }
  .brand__text { display: flex; flex-direction: column; }
  .brand__name {
    font-size: 40px;
    font-weight: 700;
    line-height: 1;
    white-space: nowrap;
  }
  .brand__tagline {
    font-size: 18px;
    font-weight: 400;
    line-height: 1;
    margin-top: 8px;
    white-space: nowrap;
  }
  .offer {
    position: absolute;
    left: 470px;
    top: 20px;
    width: 540px;
    color: var(--white);
    text-align: center;
  }
  .offer__headline { font-size: 58px; font-weight: 400; line-height: 1; white-space: nowrap; }
  .offer__sub { font-size: 28px; font-weight: 400; line-height: 1; margin-top: 8px; white-space: nowrap; }
  .seats-badge {
    position: absolute;
    left: 1026px;
    top: 14px;
    width: 158px;
    height: 114px;
    border-radius: 14px;
    border: 2px solid var(--purple-edge);
    background: linear-gradient(180deg, var(--purple-top), var(--purple-bottom));
    box-shadow: inset 0 2px 0 rgba(255,255,255,.35);
    color: var(--white);
    display: flex;
    flex-direction: column;
    align-items: center;
    justify-content: center;
    line-height: 1.1;
  }
  .seats-badge__main { font-size: 38px; }
  .seats-badge__rest { font-size: 24px; white-space: nowrap; }
</style>
</head>
<body>
  <div class="banner">
    <svg class="banner__backdrop" width="1200" height="148" viewBox="0 0 1200 148" aria-hidden="true">
      <defs>
        <linearGradient id="panelFill" x1="0" y1="0" x2="0" y2="1">
          <stop offset="0" stop-color="#ffffff"/>
          <stop offset="1" stop-color="#ececec"/>
        </linearGradient>
      </defs>
      <polygon points="0,0 428,0 458,148 0,148" fill="var(--shadow-grey)"/>
      <polygon points="0,0 412,0 440,148 0,148" fill="url(#panelFill)"/>
    </svg>

    <div class="brand">
      <span class="brand__dot"></span>
      <div class="brand__text">
        <span class="brand__name">MindHarbor 2013</span>
        <span class="brand__tagline">Conference &amp; e-Expo, August</span>
      </div>
    </div>

    <div class="offer">
      <p class="offer__headline">Buy tickets and ask</p>
      <p class="offer__sub">your unique questions to the medical panel!</p>
    </div>

    <div class="seats-badge">
      <span class="seats-badge__main">Seats</span>
      <span class="seats-badge__rest">are limited!</span>
    </div>
  </div>
</body>
</html>
```